Brisvane Partners Web Design

Dear all
I need a web design for a financial services site. We are a broker who deals with many different financial institutions and require a clean, simple and instantly impressive site based on the colour scheme that Mockwell created for us. A landing page (www.brisvn.mx) gives an idea of the logo and clour scheme but we are looking at either a one page site with rollover text boxes or a 3 or 4 page site depending on the preference of the designer and the best user experience. The site“s purpose is to give confidence that the company exists rather than impart pages of information although we would like this to be a site that can expand over time as the company grows. For now the requirement is for a clear set of possibly changing images at the centre of a white screen that relate to finance in general nad the benefits of wealth creation as well as sectios either along the top or bottom - Our Company, Our Approach, Our services, Our clients, Contact (user to fill in contact box to be sent to info@brisvn.mx. The text for each of these boxes I assume can be added by the coding team here, it the overall look and feel that I am looking for from Mockwell - deadline can be extended if necessary but I was hoping to wrap this all up in October

Target Market(s)

Succesful individuals looking to maximise returns on their investment via world class financial institutions and supported throughout by qualified independent financial advisors

Industry/Entity Type

Finance

Requirements
Must have
• Logo and color scheme of the logo design Mockwell sent - I have all these sourcefiles, pantone and fonts

```html
<!DOCTYPE html>
<html lang="en">
<head>
<meta charset="utf-8">
<title>Brisvane Partners</title>
<link href="https://fonts.googleapis.com/css2?family=Lato:ital,wght@0,400;0,700;1,400&family=Open+Sans:wght@400;600&display=swap" rel="stylesheet">
<style>
:root{
  --navy:#1d3a6a;
  --ink:#333;
  --text:#6f6f6f;
  --muted:#9a9a9a;
  --band:#f2f3f2;
  --line:#e2e2e2;
  --accent:#f0a030;
  --footer:#3b3b3b;
  --footer-deep:#2f2f2f;
  --footer-text:#9b9b9b;
}
*{margin:0;padding:0;box-sizing:border-box}
html,body{width:889px;height:1200px;overflow:hidden;background:#fff}
body{position:relative;font-family:'Lato',sans-serif;color:var(--text)}
a{color:inherit;text-decoration:none}
.abs{position:absolute}

/* header */
.site-header{position:absolute;left:0;top:0;width:889px;height:84px;background:#fff;box-shadow:0 6px 14px rgba(0,0,0,.05)}
.brand{position:absolute;left:112px;top:6px;width:110px;text-align:center;color:var(--navy);font-family:'Lato',sans-serif;font-weight:400}
.brand-mark{width:34px;height:34px;border-radius:50%;background:var(--navy);margin:0 auto 4px}
.brand-name{font-size:11px;letter-spacing:5px;line-height:13px;padding-left:5px}
.brand-sub{font-size:5px;letter-spacing:2.4px;line-height:7px;padding-left:2px}
.main-nav{position:absolute;top:40px;left:412px;display:flex;gap:0;font-size:10.5px;color:#222}
.main-nav a{margin-right:19px}
.main-nav a.active{color:var(--navy)}

/* hero */
.hero{position:absolute;left:104px;top:115px;width:683px;height:316px;overflow:hidden;
  background:linear-gradient(180deg,#c9a789 0%,#d9a574 18%,#8d7462 36%,#4e4846 60%,#2f2f31 100%)}
.hero-glow{position:absolute;inset:0;background:radial-gradient(ellipse at 22% 22%,rgba(255,205,140,.55),transparent 55%)}
.hero-ring{position:absolute;left:242px;top:-8px;width:232px;height:232px;border:2px solid rgba(255,255,255,.22);border-radius:50%}
.hero-title{position:absolute;left:0;right:0;top:156px;text-align:center;font-family:'Open Sans',sans-serif;font-size:22.5px;color:#fff;letter-spacing:-.2px}
.hero-sub{position:absolute;left:110px;right:110px;top:195px;text-align:center;font-family:'Open Sans',sans-serif;font-size:9.5px;line-height:11px;color:#fff}

/* services */
.services{position:absolute;left:104px;top:431px;width:683px;height:202px;background:var(--band)}
.service{position:absolute;top:37px;width:200px;text-align:center}
.service-icon{width:51px;height:51px;background:var(--navy);margin:0 auto;display:flex;align-items:center;justify-content:center}
.service h3{font-weight:400;font-size:13.5px;color:var(--ink);margin-top:13px}
.service p{font-size:9.2px;line-height:15.5px;margin-top:11px;color:#777}

/* about + news */
.section-title{font-weight:400;font-size:14px;color:var(--ink)}
.about{position:absolute;left:118px;top:652px;width:434px}
.about p{font-size:8.9px;line-height:15.4px;margin-top:10px;color:#6f6f6f}
.about p + p{margin-top:14px}
.about .lead{color:var(--navy)}
.more-link{position:absolute;font-size:9px;color:var(--navy)}
.more-link::before{content:"→";margin-right:6px}
.news{position:absolute;left:563px;top:652px;width:208px}
.news-item{position:relative;padding-left:42px;min-height:76px;margin-top:12px;border-bottom:1px solid var(--line)}
.news-item + .news-item{border-bottom:none;margin-top:10px}
.news-thumb{position:absolute;left:0;top:5px;width:34px;height:34px;background:linear-gradient(180deg,#c7a47e,#5e5754 60%,#3a3a3c)}
.news-item h4{font-size:8.9px;line-height:14px;color:var(--ink);font-weight:700}
.news-item time{display:block;font-size:7px;font-style:italic;color:#b5b5b5;margin-top:1px}
.news-item p{font-size:8.9px;line-height:14px;color:#888;margin-top:1px}

.separator{position:absolute;left:60px;top:876px;width:769px;height:8px;background:radial-gradient(ellipse at 50% 0,rgba(0,0,0,.07),transparent 70%)}

/* testimonials */
.testimonials{position:absolute;left:122px;top:898px;width:318px}
.quote-box{position:absolute;left:0;top:30px;width:316px;height:76px;background:#fff;box-shadow:0 1px 4px rgba(0,0,0,.18)}
.quote-box::after{content:"";position:absolute;left:20px;bottom:-16px;border-left:0 solid transparent;border-right:22px solid transparent;border-top:16px solid #fff;filter:drop-shadow(0 2px 1px rgba(0,0,0,.12))}
.quote-mark{position:absolute;left:8px;top:2px;font-family:Georgia,serif;font-size:34px;color:#ddd;line-height:34px}
.client-badge{position:absolute;left:32px;top:18px;width:38px;height:36px;border:1px solid #ddd;display:flex;align-items:center;justify-content:center}
.client-badge span{width:22px;height:22px;background:#c8202e}
.quote-text{position:absolute;left:78px;right:10px;top:12px;text-align:right;font-style:italic;font-size:8.8px;line-height:12.5px;color:#666}
.quote-author{position:absolute;left:41px;top:117px;font-size:8.3px;color:#666}
.quote-author strong{font-weight:400;color:var(--navy)}
.dots{position:absolute;left:272px;top:119px;display:flex;gap:3px}
.dots i{width:6px;height:6px;border-radius:50%;background:#ddd}
.dots i:first-child{background:var(--accent)}
.all-link{position:absolute;font-size:8.3px;color:var(--navy)}

/* partners */
.partners{position:absolute;left:456px;top:898px;width:305px}
.partner-grid{position:absolute;left:14px;top:29px;display:grid;grid-template-columns:88px 88px 88px;column-gap:15px;row-gap:11px}
.partner{width:88px;height:49px;border:1px solid #ddd;display:flex;align-items:center;justify-content:center}
.partner span{display:block;background:#d7d7d7}

/* footer */
.site-footer{position:absolute;left:0;top:1086px;width:889px;height:86px;background:var(--footer)}
.footer-nav{position:absolute;left:120px;top:25px;font-size:6.8px;color:var(--footer-text);letter-spacing:.2px}
.footer-nav a{padding:0 3px}
.footer-nav a:first-child{padding-left:0}
.footer-nav .sep{color:#666}
.footer-nav a.active{color:var(--accent)}
.footer-rule{position:absolute;top:43px;height:1px;background:#4a4a4a}
.contact-line{position:absolute;top:52px;left:119px;display:flex;gap:26px;font-size:7.8px;color:var(--footer-text);align-items:center}
.contact-line span{display:flex;align-items:center;gap:6px}
.stay{position:absolute;left:619px;top:25px;font-size:6.8px;color:var(--footer-text)}
.social{position:absolute;left:620px;top:52px;display:flex;gap:13px}
.social i{width:11px;height:11px;border-radius:2px;background:#6a6a6a}
.social i.on{background:var(--accent)}
.legal-bar{position:absolute;left:0;top:1172px;width:889px;height:28px;background:var(--footer-deep);font-size:7.8px;color:#8d8d8d}
.legal-bar p{position:absolute;left:118px;top:10px}
.legal-bar .sep{color:#555;margin:0 6px}
</style>
</head>
<body>

<header class="site-header">
  <a class="brand" href="#">
    <div class="brand-mark"></div>
    <div class="brand-name">BRISVANE</div>
    <div class="brand-sub">PARTNERS</div>
  </a>
  <nav class="main-nav">
    <a class="active" href="#">Home</a>
    <a href="#">Our Company</a>
    <a href="#">Our Approach</a>
    <a href="#">Services</a>
    <a href="#">Clients</a>
    <a href="#">Contact</a>
  </nav>
</header>

<section class="hero" role="img" aria-label="City skyline at sunset seen from above, towers under a warm evening sky">
  <div class="hero-glow"></div>
  <div class="hero-ring"></div>
  <h1 class="hero-title">Lorem ipsum dolor sit amet, consectetuer adipiscing elit.</h1>
  <p class="hero-sub">Aenean posuere, tortor sed cursus feugiat, nunc augue blandit nunc, eu sollicitudin urna dolor sagittis lacus. Donec elit libero, sodales nec, volutpat a, suscipit non, turpis.</p>
</section>

<section class="services">
  <article class="service" style="left:13px">
    <div class="service-icon">
      <svg width="20" height="22" viewBox="0 0 20 22" fill="none" stroke="#fff" stroke-width="2"><path d="M10 2a6 6 0 0 0-3.5 10.9V15h7v-2.1A6 6 0 0 0 10 2z"/><path d="M7 18h6M8 20.5h4"/></svg>
    </div>
    <h3>Service 1</h3>
    <p>Phasellus vehicula justo eget diam<br>posuere sollicitudin eu tincidunt nulla.<br>Curabitur eleifend tempor.</p>
  </article>
  <article class="service" style="left:243px">
    <div class="service-icon">
      <svg width="20" height="22" viewBox="0 0 20 22" fill="#fff"><path d="M16 2c-6 1-10 5-11 12l-2 6 1.5.5 1.8-4.5c5-.5 8.5-4 9.7-14z"/></svg>
    </div>
    <h3>Service 2</h3>
    <p>Phasellus vehicula justo eget diam<br>posuere sollicitudin eu tincidunt nulla.<br>Curabitur eleifend tempor.</p>
  </article>
  <article class="service" style="left:472px">
    <div class="service-icon">
      <svg width="22" height="22" viewBox="0 0 22 22" fill="#fff"><path d="M19 3c-5 0-9 3-11 7l4 4c4-2 7-6 7-11z"/><path d="M7 11l-4 1 3-4h4zM11 15l-1 4 4-3v-4z"/><path d="M6 14l2 2-4 3z"/></svg>
    </div>
    <h3 style="margin-top:15px">Service 3</h3>
    <p style="margin-top:9px">Phasellus vehicula justo eget diam<br>posuere sollicitudin eu tincidunt nulla.<br>Curabitur eleifend tempor.</p>
  </article>
</section>

<section class="about">
  <h2 class="section-title">Who We Are</h2>
  <p>Etiam rhoncus. Maecenas tempus, tellus eget condimentum rhoncus, sem quam semper libero, sit amet adipiscing sem neque sed ipsum. Nam quam nunc, blandit vel, luctus pulvinar, hendrerit id, lorem. Maecenas nec odio et ante tincidunt tempus. Donec vitae sapien ut libero venenatis faucibus. Nullam quis ante. Etiam sit amet orci eget eros faucibus tincidunt. Duis leo. Sed fringilla mauris sit amet nibh.</p>
  <p><span class="lead">Donec sodales sagittis magna.</span> Sed consequat, leo eget bibendum sodales, augue velit cursus nunc, quis gravida magna mi a libero. Fusce vulputate eleifend sapien. Vestibulum purus quam, scelerisque ut, mollis sed, nonummy id, metus. Nullam accumsan lorem in dui.<br>Nam pretium turpis et arcu. Duis arcu tortor, suscipit eget, imperdiet nec, imperdiet iaculis, ipsum. Sed aliquam ultrices mauris. Integer ante arcu, accumsan a, consectetuer eget, posuere ut, mauris.</p>
</section>
<a class="more-link" href="#" style="left:118px;top:847px">Learn More</a>

<section class="news">
  <h2 class="section-title">Latest News</h2>
  <article class="news-item">
    <div class="news-thumb" role="img" aria-label="City skyline thumbnail"></div>
    <h4>Curabitur ligula sapien, tincidunt non, euismod vitae.</h4>
    <time>December 12, 2013 - 9:11 pm</time>
    <p>Etiam porta est quis nulla pulvinar ultrices. Spendisse nec est acurpis.</p>
  </article>
  <article class="news-item">
    <div class="news-thumb" role="img" aria-label="City skyline thumbnail"></div>
    <h4>In dui magna, posuere eget, vestibulum et, tempor auctor, justo.</h4>
    <time>December 12, 2013 - 9:11 pm</time>
    <p>Etiam porta est quis nulla pulvinar ultrices. Spendisse nec est acurpis.</p>
  </article>
</section>
<a class="more-link" href="#" style="left:564px;top:847px">All News</a>

<div class="separator"></div>

<section class="testimonials">
  <h2 class="section-title">Testimonials</h2>
  <div class="quote-box">
    <div class="quote-mark">“</div>
    <div class="client-badge"><span></span></div>
    <p class="quote-text">Nam pretium turpis et arcu. Duis arcu tortor, suscipit eget, imperdiet nec, imperdiet iaculis, ipsum. Sed aliquam ultrices mauris. Integer ante arcu, accumsan a, consectetuer eget, posuere ut, mauris. Praesent adipiscing.</p>
  </div>
  <p class="quote-author"><strong>Daniel Harrow,</strong> Director of Research Computing</p>
  <div class="dots"><i></i><i></i><i></i><i></i></div>
</section>
<a class="all-link" href="#" style="left:374px;top:1048px">All testimonials »</a>

<section class="partners">
  <h2 class="section-title">Our Partnerts</h2>
  <div class="partner-grid">
    <div class="partner"><span style="width:62px;height:16px"></span></div>
    <div class="partner"><span style="width:60px;height:16px;background:#c9d6cf"></span></div>
    <div class="partner"><span style="width:60px;height:14px"></span></div>
    <div class="partner"><span style="width:28px;height:24px"></span></div>
    <div class="partner"><span style="width:66px;height:14px"></span></div>
    <div class="partner"><span style="width:34px;height:34px;border-radius:50%"></span></div>
  </div>
</section>
<a class="all-link" href="#" style="left:706px;top:1048px">All Partners »</a>

<footer class="site-footer">
  <nav class="footer-nav">
    <a href="#">OUR COMPANY</a><span class="sep">|</span><a class="active" href="#">OUR APPROACH</a><span class="sep">|</span><a href="#">SERVICES</a><span class="sep">|</span><a href="#">CLIENTS</a><span class="sep">|</span><a href="#">CONTACT</a>
  </nav>
  <div class="footer-rule" style="left:118px;width:488px"></div>
  <div class="footer-rule" style="left:618px;width:154px"></div>
  <div class="contact-line">
    <span><svg width="11" height="10" viewBox="0 0 11 10" fill="#7a7a7a"><path d="M5.5 0L0 5h1.5v5h3V7h2v3h3V5H11z"/></svg>48 Alder Row, Newbury, NY, 10482. USA</span>
    <span style="margin-left:8px"><svg width="10" height="10" viewBox="0 0 10 10" fill="#7a7a7a"><path d="M2 0l2 2.5-1 1.2c.6 1.3 1.6 2.3 2.8 2.9L7 5.5 9.5 7.5 8.2 9.5C4 9 1 6 .5 1.8z"/></svg>(555) 014-2290</span>
    <span style="margin-left:4px"><svg width="11" height="8" viewBox="0 0 11 8" fill="#7a7a7a"><path d="M0 0h11v8H0z"/><path d="M0 0l5.5 4.5L11 0" stroke="#3b3b3b" fill="none"/></svg>contact@brisvn.mx</span>
  </div>
  <p class="stay">STAY CONNECTED</p>
  <div class="social"><i></i><i></i><i></i><i class="on"></i><i></i><i></i></div>
</footer>

<div class="legal-bar">
  <p>Brisvane © 2013<span class="sep">|</span>Legal Notice<span class="sep">|</span>Terms</p>
</div>

</body>
</html>
```